I need a business card design for a new company that will be doing consulting work around issues of cultural competency, and diversity and inclusion. I would like the design to be crisp and clear with bold but conservative colors and incorporate shades of blue

Target Market(s)

Small businesses, schools, non-profits

Industry/Entity Type

Consulting

Font styles to use
Serif
Sans Serif

Colors
0c5ba6
6b449b
3276b5
0292cd

Requirements
Must have
• A Morrow Venture (name of company)
• Tiru Morrow
• CEO
• tiru@amorrowventure.example
• (215)555-0147

```html
<!DOCTYPE html>
<html lang="en">
<head>
<meta charset="utf-8">
<title>A Morrow Venture — Business Card</title>
<link rel="stylesheet" href="https://fonts.googleapis.com/css2?family=Playfair+Display:wght@700;900&family=Montserrat:wght@400;500&display=swap">
<style>
  :root {
    --brand-blue: #1c5fb8;
    --ink-grey: #8a8a8a;
    --ink-dark: #2b2b2b;
    --card: #f6f6f4;
    --backdrop: #dcdcdc;
    --white: #ffffff;
  }
  * { margin: 0; padding: 0; box-sizing: border-box; }
  html, body {
    width: 1200px; height: 1000px; overflow: hidden;
    background: var(--backdrop);
  }
  .canvas {
    position: relative; width: 1200px; height: 1000px;
    display: flex; align-items: center; justify-content: center;
  }
  .card {
    position: relative; width: 500px; height: 875px;
    background: var(--card);
    overflow: hidden;
    box-shadow: 0 6px 24px rgba(0,0,0,.18);
  }
  .brand-square {
    position: absolute; left: 0; top: 0;
    width: 128px; height: 128px;
    background: var(--brand-blue);
  }
  .brand-name {
    position: absolute; left: 146px; top: 24px;
    font-family: "Playfair Display", serif; font-weight: 900;
    font-size: 40px; line-height: 1.05;
    color: var(--brand-blue);
  }
  .holder-name {
    position: absolute; right: 92px; top: 312px;
    font-family: "Playfair Display", serif; font-weight: 700;
    font-size: 36px; letter-spacing: 1px;
    color: var(--brand-blue);
  }
  .holder-name .surname { color: var(--ink-grey); }
  .title-bar {
    position: absolute; right: 0; top: 362px;
    width: 250px; height: 40px;
    background: var(--brand-blue);
  }
  .title-bar .role {
    position: absolute; left: 70px; top: 50%; transform: translateY(-50%);
    font-family: "Montserrat", sans-serif; font-weight: 500;
    font-size: 22px; letter-spacing: 1px;
    color: var(--white);
  }
  .contact-line {
    position: absolute;
    font-family: "Montserrat", sans-serif; font-weight: 400;
    font-size: 19px; color: var(--ink-dark);
  }
  .contact-email { left: 150px; top: 660px; }
  .contact-phone { left: 206px; top: 700px; }
  .contact-stripe {
    position: absolute; left: 0; height: 32px;
    background: var(--brand-blue);
  }
  .stripe-email { top: 690px; width: 138px; }
  .stripe-phone { top: 728px; width: 196px; }
  .contact-icon {
    position: absolute; top: 50%; transform: translateY(-50%);
    width: 26px; height: 20px;
  }
  .stripe-email .contact-icon { right: 10px; }
  .stripe-phone .contact-icon { right: 10px; width: 22px; height: 22px; }
</style>
</head>
<body>
<main class="canvas">
  <article class="card">
    <div class="brand-square"></div>
    <h1 class="brand-name">A Morrow<br>Venture</h1>

    <h2 class="holder-name">Tiru <span class="surname">Morrow</span></h2>
    <div class="title-bar"><span class="role">CEO</span></div>

    <p class="contact-line contact-email">tiru@amorrowventure.example</p>
    <p class="contact-line contact-phone">(215)555-0147</p>

    <div class="contact-stripe stripe-email">
      <svg class="contact-icon" viewBox="0 0 26 20" aria-hidden="true">
        <rect x="1" y="1" width="24" height="18" fill="none" stroke="#fff" stroke-width="2"/>
        <path d="M1 1 L13 11 L25 1" fill="none" stroke="#fff" stroke-width="2"/>
      </svg>
    </div>
    <div class="contact-stripe stripe-phone">
      <svg class="contact-icon" viewBox="0 0 24 24" aria-hidden="true">
        <path fill="#fff" d="M6.6 10.8c1.4 2.8 3.8 5.1 6.6 6.6l2.2-2.2c.3-.3.7-.4 1-.2 1.1.4 2.3.6 3.6.6.6 0 1 .4 1 1V20c0 .6-.4 1-1 1C10.6 21 3 13.4 3 4c0-.6.4-1 1-1h3.5c.6 0 1 .4 1 1 0 1.3.2 2.5.6 3.6.1.3 0 .7-.2 1l-2.3 2.2z"/>
      </svg>
    </div>
  </article>
</main>
</body>
</html>
```